New Business Card Design Project

We want a modern business card that catches the attention of other remodeling companies as well as homeowners. We would like it to be informative but still simple.

Target Market(s)

Residential and other Business's

Contact Information for Business Card

TrellBrix
Phone number is 7263927048
Address is
4817 SW 3rd Lane
Harlow Bend, Kestria 61842
email is trellbrixco@quamlet.com

Requirements
Must have
• Our tagline
• Honest | Professional | Affordable

```html
<!DOCTYPE html>
<html lang="en">
<head>
<meta charset="utf-8">
<title>TrellBrix Business Card</title>
<link rel="stylesheet" href="https://fonts.googleapis.com/css2?family=Montserrat:wght@800&family=Oswald:wght@500&family=Lato:wght@400&display=swap">
<style>
  :root {
    --backdrop: #1e1e1e;
    --brand-orange: #cf5200;
    --brand-blue: #1a6ac8;
    --card-white: #ffffff;
    --text-dark: #3a3a3a;
    --divider: #d8d8d8;
  }
  * { margin: 0; padding: 0; box-sizing: border-box; }
  html, body {
    width: 1200px;
    height: 900px;
    overflow: hidden;
    background: var(--backdrop);
  }
  .sheet {
    position: relative;
    width: 1200px;
    height: 900px;
  }
  .card {
    position: absolute;
    left: 300px;
    width: 600px;
    height: 343px;
    box-shadow: 0 10px 30px rgba(0,0,0,0.5);
  }
  .card-front {
    top: 80px;
    background: var(--brand-orange);
    display: flex;
    flex-direction: column;
    align-items: center;
    justify-content: center;
  }
  .card-back {
    top: 477px;
    background: var(--card-white);
  }
  .wordmark {
    font-family: 'Montserrat', sans-serif;
    font-weight: 800;
    letter-spacing: 1px;
    text-transform: uppercase;
    white-space: nowrap;
  }
  .card-front .wordmark {
    color: var(--card-white);
    font-size: 56px;
    margin-top: 30px;
  }
  .tagline {
    font-family: 'Oswald', sans-serif;
    font-weight: 500;
    color: var(--card-white);
    font-size: 15px;
    letter-spacing: 1.5px;
    text-transform: uppercase;
    margin-top: 64px;
  }
  .card-back .wordmark {
    position: absolute;
    left: 40px;
    top: 196px;
    color: var(--brand-blue);
    font-size: 40px;
  }
  .divider {
    position: absolute;
    left: 318px;
    top: 60px;
    width: 1px;
    height: 150px;
    background: var(--divider);
  }
  .contact {
    position: absolute;
    left: 338px;
    top: 50px;
    font-family: 'Lato', sans-serif;
    color: var(--text-dark);
    font-size: 16px;
    line-height: 1.35;
    white-space: nowrap;
  }
  .contact-line {
    display: flex;
    align-items: center;
    gap: 7px;
  }
  .contact-icon { width: 17px; height: 17px; flex: none; }
  .contact-name {
    color: var(--brand-blue);
    text-transform: uppercase;
    margin-top: 4px;
    letter-spacing: 0.5px;
  }
</style>
</head>
<body>
<main class="sheet">
  <section class="card card-front">
    <div class="wordmark">TrellBrix</div>
    <div class="tagline">Honest | Professional | Affordable</div>
  </section>

  <section class="card card-back">
    <div class="wordmark">TrellBrix</div>
    <div class="divider"></div>
    <div class="contact">
      <div class="contact-line">
        <svg class="contact-icon" viewBox="0 0 18 18" aria-hidden="true">
          <rect x="1" y="1" width="16" height="16" rx="2" fill="none" stroke="#1a6ac8" stroke-width="1.6"/>
          <path d="M6 4.5l1.6 2.4-1 1a6 6 0 0 0 3.5 3.5l1-1 2.4 1.6-.8 1.6c-3.8-.3-7.5-4-7.8-7.8z" fill="#1a6ac8"/>
        </svg>
        <span>7263927048</span>
      </div>
      <div class="contact-line">
        <svg class="contact-icon" viewBox="0 0 18 18" aria-hidden="true">
          <rect x="1" y="4" width="16" height="11" fill="#1a6ac8"/>
          <path d="M1 4l8 6 8-6" fill="none" stroke="#fff" stroke-width="1.4"/>
        </svg>
        <span>trellbrixco@quamlet.com</span>
      </div>
      <div class="contact-name">TrellBrix</div>
      <div class="contact-address">4817 SW 3rd Lane<br>Harlow Bend, Kestria 61842</div>
    </div>
  </section>
</main>
</body>
</html>
```